Dalvor Inc Business Card

Looking to get an updated business card for a Contract Machining company (www.dalvorinc-example.com) - looking for a clean design the portrays the technical nature of the business - colors can follow the website design and be in any combination that makes sense (red black, white, metallic or silver) - logos attached for use also. Would like space for: Name, title, business phone (555 214-3098), cell phone , website (www.dalvorinc-example.com) - possibly QR code could be integrated for website (designer choice), business address - 418 Birchfield Lane, Alderbrook, OH 43950 (cards will be for 4 employees, I will either need to modify a template or I can provide individual information)
Target Market(s)
Aerospace, defense and medical device manufacturing companies that need machining
Industry/Entity Type
Machining for aerospace, defense, medical
Contact Information for Business Card
Name, Title, Business Phone, Cell Phone, email, business website and business address

```html
<!DOCTYPE html>
<html lang="en">
<head>
<meta charset="utf-8">
<title>Dalvor Inc Business Card</title>
<link href="https://fonts.googleapis.com/css2?family=Montserrat:wght@400;500;800&display=swap" rel="stylesheet">
<style>
  :root {
    --red: #b51f24;
    --black: #151515;
    --white: #ffffff;
    --backdrop: #d9d9d9;
  }
  html, body {
    margin: 0;
    padding: 0;
    width: 1200px;
    height: 900px;
    overflow: hidden;
    background: var(--backdrop);
    font-family: "Montserrat", sans-serif;
  }
  .canvas {
    position: relative;
    width: 1200px;
    height: 900px;
  }
  .card {
    position: absolute;
    left: 290px;
    width: 620px;
    height: 354px;
    border-radius: 20px;
    overflow: hidden;
    box-shadow: 0 10px 28px rgba(0,0,0,0.25);
  }
  .card-back {
    top: 60px;
    background: var(--black);
  }
  .back-pattern {
    position: absolute;
    inset: 0;
    background: linear-gradient(100deg, #8d8d8d 0%, #4a4a4a 35%, #1c1c1c 60%, #0b0b0b 100%);
  }
  .card-front {
    top: 476px;
    background: var(--white);
  }
  .disc-outer {
    position: absolute;
    left: 280px;
    top: -110px;
    width: 430px;
    height: 430px;
    border-radius: 50%;
    background: var(--black);
  }
  .disc-inner {
    position: absolute;
    left: 314px;
    top: -72px;
    width: 356px;
    height: 356px;
    border-radius: 50%;
    background: var(--red);
  }
  .disc-name {
    position: absolute;
    left: 314px;
    top: 88px;
    width: 306px;
    text-align: center;
    font-weight: 800;
    font-size: 28px;
    letter-spacing: 1px;
    color: var(--black);
  }
  .company-name {
    position: absolute;
    left: 30px;
    top: 32px;
    margin: 0;
    font-weight: 800;
    font-size: 28px;
    letter-spacing: 0.5px;
    color: var(--red);
    white-space: nowrap;
  }
  .accent-bar {
    position: absolute;
    left: 0;
    top: 112px;
    width: 14px;
    height: 52px;
    background: var(--red);
  }
  .person-name {
    position: absolute;
    left: 30px;
    top: 108px;
    margin: 0;
    font-weight: 800;
    font-size: 26px;
    color: var(--red);
    letter-spacing: 0.5px;
    white-space: nowrap;
  }
  .person-title {
    position: absolute;
    left: 30px;
    top: 142px;
    margin: 0;
    font-weight: 500;
    font-size: 17px;
    color: var(--black);
  }
  .address {
    position: absolute;
    left: 30px;
    top: 182px;
    margin: 0;
    font-style: normal;
    font-weight: 400;
    font-size: 16px;
    line-height: 22px;
    color: var(--black);
  }
  .contacts {
    position: absolute;
    left: 30px;
    top: 242px;
    margin: 0;
    padding: 0;
    list-style: none;
  }
  .contacts li {
    display: flex;
    align-items: center;
    gap: 10px;
    height: 23px;
    font-size: 15px;
    color: var(--black);
    white-space: nowrap;
  }
  .contacts svg {
    width: 15px;
    height: 15px;
    flex: none;
  }
</style>
</head>
<body>
<main class="canvas">

  <section class="card card-back" aria-label="Card back">
    <div class="back-pattern" role="img" aria-label="Repeating pattern of company emblem discs fading from silver to black"></div>
  </section>

  <section class="card card-front" aria-label="Card front">
    <div class="disc-outer"></div>
    <div class="disc-inner"></div>
    <div class="disc-name">DALVOR INC</div>

    <h1 class="company-name">DALVOR INC.</h1>

    <div class="accent-bar"></div>
    <h2 class="person-name">MARCUS HALE</h2>
    <p class="person-title">Managing Director</p>

    <address class="address">418 Birchfield Lane,<br>Alderbrook, OH 43950</address>

    <ul class="contacts">
      <li>
        <svg viewBox="0 0 16 16" aria-hidden="true"><path fill="#b51f24" d="M3.5 1.5l2.5 3-1.5 1.8c.8 1.8 2.2 3.2 4 4l1.8-1.5 3 2.5-1.6 2.4C6.8 13.2 2.8 9.2 1.3 3.1z"/></svg>
        <span>(555 214-3098</span>
      </li>
      <li>
        <svg viewBox="0 0 16 16" aria-hidden="true"><rect x="4" y="1" width="8" height="14" rx="1.5" fill="none" stroke="#b51f24" stroke-width="1.6"/><circle cx="8" cy="12.5" r="0.9" fill="#b51f24"/></svg>
        <span>555-367-1042</span>
      </li>
      <li>
        <svg viewBox="0 0 16 16" aria-hidden="true"><rect x="1" y="3" width="14" height="10" rx="1" fill="#b51f24"/><path d="M1.5 3.8L8 9l6.5-5.2" fill="none" stroke="#fff" stroke-width="1.3"/></svg>
        <span>info@dalvorinc-example.com</span>
      </li>
      <li>
        <svg viewBox="0 0 16 16" aria-hidden="true"><circle cx="8" cy="8" r="6.5" fill="#b51f24"/><path d="M1.5 8h13M8 1.5c-2.5 3-2.5 10 0 13M8 1.5c2.5 3 2.5 10 0 13" fill="none" stroke="#fff" stroke-width="1"/></svg>
        <span>www.dalvorinc-example.com</span>
      </li>
    </ul>
  </section>

</main>
</body>
</html>
```